Velloria Flowers Florist Flyer

We are requiring a flyer that advertises and promotes our new business. We specialise in weddings and events but would also like to branch out to corporates and an online subscription. Our brand is feminine/romantic with a touch of elegance and luxury. Our main colour schemes are white, black, gold and pale pink. Instagram: Velloria_flowers and website www.velloriaflowers.com.au
Target Market(s)
brides to be, females
Industry/Entity Type
Florist
Font styles to use
Sans Serif
Script
Other font styles liked:
- The Carpenter
Colors
ffffff
000000
333333
Requirements
Must have
- Feminine/romantic feel, through use of theme colours and elegant font
- our contact details Ph: 0429518064
- email address: contactus@velloriaflowers.com.au
Nice to have
- a description of us willing to work with clients to create their dream wedding flowers. That we offer consultations and no obligation quotes.

```html
<!DOCTYPE html>
<html lang="en">
<head>
<meta charset="utf-8">
<title>Velloria Flowers – Flyer</title>
<link rel="stylesheet" href="https://fonts.googleapis.com/css2?family=Saira:wght@300&family=Roboto+Condensed:wght@400&family=Josefin+Sans:wght@400&display=swap">
<style>
  :root {
    --canvas: #eceef2;
    --pink: #e3a9cf;
    --ink: #1d1a1c;
    --white: #ffffff;
    --rule: #6d5066;
    --photo-dark: #2a2e2c;
    --photo-stone: #b9bcba;
    --photo-rose: #a8343a;
    --photo-blush: #e9c2b4;
    --photo-leaf: #3f5a36;
  }
  * { margin: 0; padding: 0; box-sizing: border-box; }
  html, body { width: 1012px; height: 1200px; overflow: hidden; }
  body {
    background: var(--canvas);
    position: relative;
    font-family: "Roboto Condensed", "Arial Narrow", sans-serif;
    color: var(--ink);
  }
  .card {
    position: absolute;
    left: 121px;
    width: 770px;
    box-shadow: 0 4px 14px rgba(0,0,0,.18);
  }
  .card--front {
    top: 50px;
    height: 540px;
    background: linear-gradient(120deg, var(--photo-leaf) 0%, var(--photo-stone) 28%, var(--photo-dark) 50%, var(--photo-stone) 72%, var(--photo-rose) 100%);
  }
  .card--back {
    top: 620px;
    height: 530px;
    background: var(--pink);
  }
  .headline {
    position: absolute;
    left: 50px; top: 38px;
    width: 420px;
    font-family: "Saira", sans-serif;
    font-weight: 300;
    font-size: 24px;
    line-height: 32px;
    letter-spacing: 2.4px;
    color: var(--white);
    text-transform: uppercase;
  }
  .intro {
    position: absolute;
    left: 50px; top: 118px;
    width: 380px;
    font-size: 15.5px;
    line-height: 20px;
  }
  .gallery {
    position: absolute;
    left: 5px; top: 212px;
    display: flex; gap: 3px;
  }
  .gallery__photo { width: 145px; height: 86px; }
  .gallery__photo--pink { background: linear-gradient(135deg, #f3c7cf, #d9849a 60%, #8ea67a); }
  .gallery__photo--cream { background: linear-gradient(135deg, #e4c9a4, #f0eee0 50%, #5e7450); }
  .gallery__photo--red { background: linear-gradient(135deg, #5a1a22, #b22a33 50%, #e8e2d6); }
  .divider {
    position: absolute;
    left: 457px; top: 35px;
    width: 1px; height: 455px;
    background: var(--rule);
  }
  .testimonial {
    position: absolute;
    left: 470px; top: 176px;
    width: 232px;
    text-align: center;
  }
  .testimonial__mark {
    display: inline-block;
    width: 20px; height: 20px;
    border: 1px solid var(--ink);
    border-radius: 50%;
    font-size: 10px; line-height: 18px;
  }
  .testimonial__title {
    margin-top: 6px;
    font-family: "Saira", sans-serif;
    font-weight: 300;
    font-size: 13px;
    letter-spacing: 2px;
  }
  .testimonial__quote {
    margin-top: 10px;
    font-size: 11.5px;
    line-height: 15px;
  }
  .testimonial__author {
    margin-top: 5px;
    font-size: 7.5px;
    letter-spacing: 1px;
    text-transform: uppercase;
  }
  .brand {
    position: absolute;
    left: 470px; top: 388px;
    width: 232px;
    text-align: center;
  }
  .brand__name {
    font-family: "Josefin Sans", sans-serif;
    font-size: 26px;
    letter-spacing: 4px;
    text-transform: uppercase;
    line-height: 30px;
  }
  .brand__copyright {
    margin-top: 12px;
    font-size: 7.5px;
    letter-spacing: 1.2px;
    text-transform: uppercase;
  }
  .contacts {
    position: absolute;
    left: 45px; top: 448px;
    display: flex; gap: 34px;
  }
  .contact { display: flex; align-items: flex-start; gap: 8px; }
  .contact__icon { width: 20px; height: 20px; margin-top: 3px; }
  .contact__label {
    font-size: 10px; letter-spacing: 1px; text-transform: uppercase;
    line-height: 12px;
  }
  .contact__value { font-size: 12px; line-height: 14px; }
</style>
</head>
<body>
  <div class="card card--front" role="img" aria-label="Photograph of a round black shop sign on a tiled wall, framed by lush arrangements of red and blush roses with greenery"></div>

  <div class="card card--back">
    <h1 class="headline">Looking for flowers for a wedding or event?</h1>
    <p class="intro">We specialise in flowers for weddings and events. No matter how big or small we’re here to create the best looking flowers just for you.</p>

    <div class="gallery">
      <div class="gallery__photo gallery__photo--pink" role="img" aria-label="Bouquet of pink roses"></div>
      <div class="gallery__photo gallery__photo--cream" role="img" aria-label="Bouquet of peach and cream roses with greenery"></div>
      <div class="gallery__photo gallery__photo--red" role="img" aria-label="Bouquet of deep red and white roses"></div>
    </div>

    <div class="divider"></div>

    <div class="testimonial">
      <span class="testimonial__mark">99</span>
      <h2 class="testimonial__title">WHAT PEOPLE SAY?</h2>
      <p class="testimonial__quote">Thank you for creating the most beautiful flowers I could ever dream of. You helped me design something that is truly meaningful and is absolutely stunning.</p>
      <p class="testimonial__author">— Marina Holloway, recently married</p>
    </div>

    <div class="brand">
      <p class="brand__name">Velloria Flowers</p>
      <p class="brand__copyright">© Velloria Flowers 2018</p>
    </div>

    <div class="contacts">
      <div class="contact">
        <svg class="contact__icon" viewBox="0 0 20 20" aria-hidden="true">
          <rect x="3" y="3" width="14" height="14" transform="rotate(45 10 10)" fill="#1d1a1c"/>
          <path d="M7.5 6.5 l1.5 0 l0.7 2 l-1 0.8 a5 5 0 0 0 2 2 l0.8 -1 l2 0.7 l0 1.5 a1 1 0 0 1 -1 1 a7 7 0 0 1 -6 -6 a1 1 0 0 1 1 -1z" fill="#e3a9cf"/>
        </svg>
        <div>
          <p class="contact__label">Call us</p>
          <p class="contact__value">+61 4 295 180 64</p>
        </div>
      </div>
      <div class="contact">
        <svg class="contact__icon" viewBox="0 0 20 20" aria-hidden="true">
          <rect x="3" y="3" width="14" height="14" transform="rotate(45 10 10)" fill="#1d1a1c"/>
          <rect x="6" y="7" width="8" height="6" fill="none" stroke="#e3a9cf" stroke-width="1"/>
          <path d="M6 7 l4 3.2 l4 -3.2" fill="none" stroke="#e3a9cf" stroke-width="1"/>
        </svg>
        <div>
          <p class="contact__label">Email</p>
          <p class="contact__value">contactus@velloriaflowers.com.au</p>
        </div>
      </div>
    </div>
  </div>
</body>
</html>
```